high end contractor

high end contracting company we do all phases of construction kitchen,bathrooms,etc... please look at my website before you design www.harborkeybuild.com

would love some sort of lines or logo or both

Industry/Entity Type

Construction

Contact Information for Business Card

company name: oak & meridian contracting address: 318 fenwick st Eastbrook NY 10587 email: harborkeybuild@mailbrook.com website: www.harborkeybuild.com office#: 914-208-3916 fax#: 914-208-5523 dominic valtersen mobile# 917-526-0389

```html
<!DOCTYPE html>
<html lang="en">
<head>
<meta charset="utf-8">
<title>Oak &amp; Meridian – Business Card</title>
<link rel="stylesheet" href="https://fonts.googleapis.com/css2?family=Questrial&display=swap">
<style>
  :root {
    --page: #e9e6e1;
    --card-front: #222222;
    --card-back: #333333;
    --band: #3b3b3b;
    --name-band: #1e1e1e;
    --teal: #3fb1b3;
    --text-light: #e4e4e4;
    --text-muted: #c9c9c9;
  }
  * { margin: 0; padding: 0; box-sizing: border-box; }
  html, body { width: 1200px; height: 456px; overflow: hidden; }
  body {
    background: var(--page);
    font-family: "Questrial", "Century Gothic", sans-serif;
    position: relative;
  }
  .card {
    position: absolute;
    top: 138px;
    width: 288px;
    height: 185px;
    box-shadow: 0 4px 14px rgba(0,0,0,0.25);
  }
  /* Front */
  .card--front { left: 175px; background: var(--card-front); }
  .front-band {
    position: absolute;
    left: 16px; right: 0;
    top: 65px; height: 54px;
    background: var(--band);
    border-left: 3px solid var(--teal);
    padding: 5px 0 0 13px;
  }
  .front-name {
    color: var(--teal);
    font-size: 20px;
    letter-spacing: 1.6px;
    line-height: 24px;
  }
  .front-url {
    color: var(--text-muted);
    font-size: 12.5px;
    letter-spacing: 2.1px;
    line-height: 18px;
  }
  /* Back */
  .card--back {
    left: 757px;
    background: var(--card-back);
    border-left: 3px solid var(--teal);
  }
  .back-title {
    position: absolute;
    left: 7px; top: 21px;
    font-size: 14.5px;
    letter-spacing: 1.2px;
    white-space: nowrap;
  }
  .back-title .company { color: var(--teal); }
  .back-title .trade { color: var(--text-light); }
  .name-band {
    position: absolute;
    left: 4px; right: 0;
    top: 55px; height: 26px;
    background: var(--name-band);
    display: flex;
    align-items: center;
    justify-content: space-between;
    padding: 0 6px 0 10px;
  }
  .person { color: var(--teal); font-size: 12px; letter-spacing: 1.2px; }
  .mobile { color: var(--text-light); font-size: 13px; letter-spacing: 0.8px; }
  .contact {
    position: absolute;
    left: 6px;
    display: flex;
    align-items: center;
    color: var(--text-light);
    font-size: 12.5px;
    letter-spacing: 0.6px;
    white-space: nowrap;
  }
  .contact--phone { top: 90px; }
  .contact--fax { top: 90px; left: 158px; }
  .contact--email { top: 117px; }
  .contact--address { top: 145px; letter-spacing: 0.4px; }
  .icon {
    width: 17px; height: 17px;
    border-radius: 50%;
    background: var(--teal);
    color: var(--card-back);
    font-size: 10px;
    font-weight: bold;
    display: inline-flex;
    align-items: center;
    justify-content: center;
    margin-right: 17px;
    flex: none;
  }
  .icon svg { display: block; }
</style>
</head>
<body>

  <section class="card card--front">
    <div class="front-band">
      <div class="front-name">OAK &amp; MERIDIAN</div>
      <div class="front-url">www.harborkeybuild.com</div>
    </div>
  </section>

  <section class="card card--back">
    <div class="back-title"><span class="company">OAK &amp; MERIDIAN</span> <span class="trade">RENOVATIONS</span></div>
    <div class="name-band">
      <span class="person">DOMINIC VALTERSEN</span>
      <span class="mobile">917-526-0389</span>
    </div>
    <div class="contact contact--phone"><span class="icon">P</span>914-208-3916</div>
    <div class="contact contact--fax"><span class="icon">F</span>914-208-5523</div>
    <div class="contact contact--email">
      <span class="icon">
        <svg width="10" height="8" viewBox="0 0 10 8"><rect x="0.5" y="0.5" width="9" height="7" fill="none" stroke="#333" stroke-width="1.2"/><path d="M0.5 0.8 L5 4.6 L9.5 0.8" fill="none" stroke="#333" stroke-width="1.2"/></svg>
      </span>harborkeybuild@mailbrook.com
    </div>
    <div class="contact contact--address">
      <span class="icon">
        <svg width="8" height="11" viewBox="0 0 8 11"><path d="M4 0.5 A3.5 3.5 0 0 1 7.5 4 C7.5 6.5 4 10.5 4 10.5 C4 10.5 0.5 6.5 0.5 4 A3.5 3.5 0 0 1 4 0.5 Z" fill="#333"/><circle cx="4" cy="4" r="1.3" fill="#3fb1b3"/></svg>
      </span>318 Fenwick st. Eastbrook NY 10587
    </div>
  </section>

</body>
</html>
```